Dynamic and Revolutionary Training Company Requires Stationery Design Project

We are a training company who deliver training both online and face to face.

We train in:
~ Industry Training: Earth Moving Machinery, Cranes, Work at Heights, Confined Spaces, Elevating Work Platforms, Forklift etc.
~ Food Hygiene / Safety
~ Responsible Service of Alcohol / Gambling

Our company is interested in sourcing stationery designs for:

* Pens
These will be used in classroom training courses but also given away in advertising 'packs'

* Presentation folders
These can be either bi or tri fold cardboard folders. Promotional materials / leaflets will be placed inside these folders and given away in advertising 'packs'

* Letterhead
We need to update our old / outdated letterhead

* Exercise Book Covers
These exercise books will be used by students in our face to face training courses.

* With Compliments Slip
In 100+ envelopes we send each day we currently add a business card. We are now going to add a with with compliments slip with an offer / promotion instead.

* Pull Up Banner
Front of stall display at expos / trade shows.

* Flyers
We would like a template design for a DL sized flyer. We offer training in over 30 courses, so if we had a standard template that could be adapted to each training course we would achieve consistency in advertising.
Flyers would need the same / similar front (with space for a picture) and course information could be placed on the back.

Because of our extensive (and ever expanding) scope of training, certain products (folders, exercise books) will allow us to list some / all our training courses.
Other advertising mediums will obviously only allow us to display our logo and slogan (pens etc).

Please find attached our company logo.
Company slogan -
Updates

Good Morning All,

I apologise for this glaring oversight.

I unfortunately failed to mention that our primary 'business colour' (obviously outside the logo) is blue. 

Traditionally, the blue I refer to is a lightish blue as can be seen on our website banner: www.quorvatraining.edu.au 
We are however moving into a new premises which has navy blue carpet, so we would like to move more towards a navy blue.

We would also like to adjust several sliders, significantly more towards:
* elegant
* personable

And somewhat more towards:
* colourful

Sorry for any inconvenience designers :(

Regards,
Tom

Closing day tomorrow.

Only received designs from 2 designers thus far.

Last chance today to submit designs.............................

Target Market(s)

Employed / unemployed persons looking to upskill, companies / organisations looking for a quality training provider.

Industry/Entity Type

Advertising

Requirements
Must have
• More than happy to be guided by designer.

I would like to see the letterhead also involve a footer - of some sort.

Logo colours are original since company inception so must remain.

Slogan - we do have one, however our advertising has never had it as a major focus.
Nice to have
• Most written correspondence we send via email (statements of attainment, invoices etc) has a Quorva Training watermark across it.
If possible and it looks appropriate in your opinion, the larger advertising (folders, exercise books) could MAYBE have that as well.

```html
<!DOCTYPE html>
<html lang="en">
<head>
<meta charset="utf-8">
<title>Quorva Training – Stationery</title>
<link rel="stylesheet" href="https://fonts.googleapis.com/css2?family=Arimo&family=Source+Sans+3:wght@400;600;700&display=swap">
<style>
  :root {
    --navy: #26418a;
    --olive: #a8a23a;
    --paper: #ffffff;
    --ink: #1c1c1c;
    --muted: #555555;
    --backdrop: #e6e4e0;
    --watermark: #f0ede3;
  }
  * { box-sizing: border-box; margin: 0; padding: 0; }
  html, body { width: 1200px; height: 849px; overflow: hidden; }
  body { background: var(--backdrop); position: relative; font-family: "Source Sans 3", sans-serif; }

  .sheet { position: absolute; background: var(--paper); }
  .letterhead { left: 46px; top: 40px; width: 595px; height: 769px; }
  .comp-slip { left: 575px; top: 400px; width: 580px; height: 272px; border: 1px solid #cfcfcf; }

  .band { position: absolute; left: 0; right: 0; background: var(--navy); }
  .letterhead .band { top: 32px; height: 76px; }
  .comp-slip .band { top: 12px; height: 76px; }

  .brand { position: absolute; right: 48px; top: 22px; display: flex; align-items: center; gap: 6px; }
  .comp-slip .brand { right: 30px; }
  .brand-square { width: 14px; height: 14px; background: var(--olive); }
  .brand-name { color: #fff; font-weight: 700; font-size: 12px; letter-spacing: 0.6px; text-transform: uppercase; }

  .slip-title { position: absolute; left: 29px; top: 26px; color: var(--olive); font-weight: 700; font-size: 19px; }

  .watermark { position: absolute; left: 166px; top: 298px; width: 264px; text-align: center; }
  .watermark-square { width: 110px; height: 110px; background: var(--watermark); margin: 0 auto 10px; }
  .watermark-name { color: var(--watermark); font-weight: 700; font-size: 27px; letter-spacing: 1px; text-transform: uppercase; }

  .letter { position: absolute; left: 49px; top: 171px; width: 500px; font-family: "Arimo", sans-serif; font-size: 12.3px; line-height: 14px; color: var(--ink); }
  .letter p { margin-bottom: 14px; }
  .letter .date { margin-bottom: 28px; }
  .letter .recipient { margin-bottom: 27px; }
  .letter .closing { margin-top: 28px; margin-bottom: 48px; }

  .footer { position: absolute; border-top: 1.5px solid var(--olive); font-size: 7px; line-height: 9px; color: var(--muted); }
  .letterhead .footer { left: 48px; width: 498px; top: 709px; }
  .comp-slip .footer { left: 29px; width: 521px; top: 230px; }
  .footer-col { position: absolute; top: 13px; white-space: nowrap; }
  .footer b { color: var(--olive); font-weight: 700; margin-right: 4px; }
  .footer .web { color: var(--olive); font-weight: 700; }
  .col-address { left: 0; }
  .col-phone { left: 128px; }
  .col-online { left: 223px; }
  .col-reg { left: 351px; }
</style>
</head>
<body>

<section class="sheet letterhead" aria-label="Letterhead">
  <header class="band">
    <div class="brand"><span class="brand-square"></span><span class="brand-name">Quorva Training</span></div>
  </header>

  <div class="watermark" aria-hidden="true">
    <div class="watermark-square"></div>
    <div class="watermark-name">Quorva Training</div>
  </div>

  <div class="letter">
    <p class="date">September 10, 2012</p>
    <p class="recipient">Ms. Carla Denning<br>Accounts Payable<br>The Copper Pan<br>412 Harbour Lane<br>Millbrook, CA 60412</p>
    <p>Dear Ms. Denning,<br>It has come to my attention that your company, The Copper Pan has been late with paying their invoices for the past three months.</p>
    <p>In order to encourage our customers to pay for their invoices before the due date, we have implemented a discount model where we'll give you 2% off your invoice if you pay us within 10 days of receiving the invoice.</p>
    <p>I hope that everything is going well for you and your company. You are one of our biggest customers, and we appreciate your business. If you have any questions, feel free to contact me at (555) 555-0142.</p>
    <p class="closing">Sincerely,</p>
    <p>Glen Ashby<br>Accounts Receivable</p>
  </div>

  <footer class="footer">
    <div class="footer-col col-address">PO Box 3150, Tannum East,<br>Queensland 4681</div>
    <div class="footer-col col-phone"><b>P</b>(07) 4138 2261<br><b>F</b>(07) 4138 2274</div>
    <div class="footer-col col-online">support@quorvatraining.edu.au<br><span class="web">www.quorvatraining.edu.au</span></div>
    <div class="footer-col col-reg"><b>ABN</b>61 204 318 905<br><b>RTO</b>47215</div>
  </footer>
</section>

<section class="sheet comp-slip" aria-label="With compliments slip">
  <header class="band">
    <h1 class="slip-title">With Compliment</h1>
    <div class="brand"><span class="brand-square"></span><span class="brand-name">Quorva Training</span></div>
  </header>

  <footer class="footer">
    <div class="footer-col col-address">PO Box 3150, Tannum East,<br>Queensland 4681</div>
    <div class="footer-col col-phone"><b>P</b>(07) 4138 2261<br><b>F</b>(07) 4138 2274</div>
    <div class="footer-col col-online">support@quorvatraining.edu.au<br><span class="web">www.quorvatraining.edu.au</span></div>
    <div class="footer-col col-reg"><b>ABN</b>61 204 318 905<br><b>RTO</b>47215</div>
  </footer>
</section>

</body>
</html>
```